Estate Planning Law Firm opening new branch in Florida

I am an experienced estate planning attorney that recently relocated to Florida. Looking for a banner Ad to place on platforms such as YardLoop, Chatterly and Pixmora to create publicity for firm and new leads.

```html
<!DOCTYPE html>
<html lang="en">
<head>
<meta charset="utf-8">
<title>Serenova Law Firm – Now in Florida</title>
<link rel="stylesheet" href="https://fonts.googleapis.com/css2?family=Lexend:wght@400;500&family=Montserrat:wght@700&family=Noto+Serif:wght@400;900&display=swap">
<style>
  :root {
    --navy: #283a4f;
    --teal: #15706e;
    --paper: #ececec;
    --mist: #dcdfe3;
    --slate: #7f8899;
    --white: #ffffff;
    --stage: #d6d6d6;
  }
  * { margin: 0; padding: 0; box-sizing: border-box; }
  html, body { width: 1200px; height: 978px; overflow: hidden; background: var(--stage); }
  .ad {
    position: absolute; left: 111px; top: 0;
    width: 978px; height: 978px;
    background: var(--paper);
    overflow: hidden;
    font-family: "Lexend", sans-serif;
    color: var(--navy);
  }
  .ad__shapes { position: absolute; inset: 0; width: 100%; height: 100%; }

  .badge {
    position: absolute; left: 235px; top: 135px;
    width: 166px; height: 166px; border-radius: 50%;
    background: var(--white);
    display: flex; flex-direction: column; align-items: center; justify-content: center;
    font-family: "Montserrat", sans-serif; font-weight: 700; color: var(--navy);
  }
  .badge__now { font-size: 48px; line-height: 1; letter-spacing: 1px; }
  .badge__place { font-size: 19px; line-height: 1.2; margin-top: 6px; }

  .firm { position: absolute; left: 566px; top: 198px; width: 352px; }
  .firm__name {
    display: flex; align-items: center; gap: 12px;
    font-family: "Noto Serif", serif; font-weight: 400;
    font-size: 50px; line-height: 1; color: var(--navy); letter-spacing: 1px;
  }
  .firm__mark { width: 26px; height: 26px; background: var(--navy); flex: none; }
  .firm__type {
    display: flex; align-items: center; gap: 8px;
    margin: 8px 0 0 70px;
    font-size: 15px; color: var(--navy); white-space: nowrap;
  }
  .firm__type::before, .firm__type::after {
    content: ""; flex: 1; height: 1px; background: var(--navy);
  }

  .headline {
    position: absolute; left: 70px; top: 348px;
    font-family: "Noto Serif", serif; font-weight: 900;
    font-size: 72px; line-height: 85px; color: var(--navy);
    white-space: nowrap;
  }
  .headline__brand { color: var(--teal); }

  .divider {
    position: absolute; left: 80px; top: 652px;
    display: flex; gap: 18px;
  }
  .divider span { width: 4px; height: 4px; border-radius: 50%; background: var(--teal); }

  .attorney { position: absolute; left: 76px; top: 700px; }
  .attorney__name { font-size: 37px; font-weight: 500; line-height: 1.2; }
  .attorney__role { font-size: 23px; font-weight: 400; line-height: 1.4; }

  .contact { position: absolute; left: 74px; top: 812px; list-style: none; }
  .contact__item {
    display: flex; align-items: center; gap: 18px;
    font-size: 25px; line-height: 37px;
  }
  .contact__icon { width: 30px; height: 30px; fill: var(--teal); flex: none; }

  .portrait-note {
    position: absolute; left: 680px; top: 578px; width: 190px;
    text-align: center;
    font-family: "Lexend", sans-serif; font-size: 40px; line-height: 50px;
    color: #c9cbcf;
  }
</style>
</head>
<body>
<div class="ad">
  <svg class="ad__shapes" viewBox="0 0 984 983" preserveAspectRatio="none">
    <defs>
      <linearGradient id="deskTone" x1="0" y1="0" x2="1" y2="1">
        <stop offset="0" stop-color="#3d5a63"/>
        <stop offset="0.5" stop-color="#9fb1b3"/>
        <stop offset="1" stop-color="#d8e2e2"/>
      </linearGradient>
      <linearGradient id="portraitTone" x1="0" y1="0" x2="0" y2="1">
        <stop offset="0" stop-color="#3a3434"/>
        <stop offset="0.45" stop-color="#4b4d55"/>
        <stop offset="1" stop-color="#2f3038"/>
      </linearGradient>
    </defs>
    <polygon class="shape-mist" points="380,290 840,108 984,190 984,460" fill="var(--mist)"/>
    <polygon class="shape-corner" points="708,0 984,0 984,192" fill="var(--teal)"/>
    <polygon class="shape-corner-edge" points="690,0 708,0 984,192 984,200" fill="var(--white)"/>
    <polygon class="desk-photo" role="img" aria-label="Photo area: hands signing documents at a desk beside a laptop" points="0,0 690,0 838,104 0,264" fill="url(#deskTone)"/>
    <polygon class="band-teal" points="0,272 838,110 842,118 0,308" fill="var(--teal)"/>
    <path class="portrait-photo" role="img" aria-label="Photo area: portrait of the estate planning attorney" d="M580,882 L592,620 L640,520 L700,460 L720,330 Q770,300 830,320 L870,440 L950,510 L984,560 L984,772 Z" fill="url(#portraitTone)"/>
    <polygon class="base-edge" points="240,983 984,762 984,790 270,983" fill="var(--white)"/>
    <polygon class="base-slate" points="270,983 984,790 984,983" fill="var(--slate)"/>
    <polygon class="base-navy" points="0,913 320,983 0,983" fill="var(--navy)"/>
  </svg>

  <div class="badge">
    <span class="badge__now">NOW</span>
    <span class="badge__place">IN FLORIDA</span>
  </div>

  <div class="firm">
    <div class="firm__name"><span class="firm__mark"></span>SERENOVA</div>
    <div class="firm__type">LAW FIRM, PLLC</div>
  </div>

  <h1 class="headline">Secure Your<br>Family's Future<br>With <span class="headline__brand">Serenova</span></h1>

  <div class="divider"><span></span><span></span><span></span><span></span><span></span><span></span><span></span><span></span></div>

  <div class="attorney">
    <p class="attorney__name">Firstname Lastname</p>
    <p class="attorney__role">Estate Planning Attorney</p>
  </div>

  <ul class="contact">
    <li class="contact__item">
      <svg class="contact__icon" viewBox="0 0 24 24" aria-hidden="true"><path d="M6.6 10.8a15.2 15.2 0 0 0 6.6 6.6l2.2-2.2c.3-.3.7-.4 1-.2 1.1.4 2.3.6 3.6.6.6 0 1 .4 1 1V20c0 .6-.4 1-1 1A17 17 0 0 1 3 4c0-.6.4-1 1-1h3.5c.6 0 1 .4 1 1 0 1.3.2 2.5.6 3.6.1.3 0 .7-.2 1z"/></svg>
      <span>31 804 2615</span>
    </li>
    <li class="contact__item">
      <svg class="contact__icon" viewBox="0 0 24 24" aria-hidden="true"><path d="M2 5h20v2l-10 6L2 7z M2 9.3l10 6 10-6V19H2z"/></svg>
      <span>email@serenova.com</span>
    </li>
  </ul>

  <p class="portrait-note">YOUR PHOTO HERE</p>
</div>
</body>
</html>
```